Pool bar in traditional boutique hotel in Crete needs a menu

We need a menu design for the new pool bar in a traditional boutique hotel called Kelari Vostina based in Chania, Crete in Greece. We serve homemade desserts, pies, salads, cocktails and fresh juices, all made with local or our products. We would like to see a menu happy and simple like us and our guests.

Target Market(s)

Families, old and young couples, gay couples

Industry/Entity Type

Boutique

```html
<!DOCTYPE html>
<html lang="en">
<head>
<meta charset="utf-8">
<title>Kelari Vostina – Pool Bar Menu</title>
<link rel="stylesheet" href="https://fonts.googleapis.com/css2?family=Source+Sans+3:wght@400;600&display=swap">
<style>
  :root {
    --paper: #ffffff;
    --crimson: #a50000;
    --crimson-deep: #4a0000;
    --crimson-title: #8a0000;
    --blush: #e07a7a;
    --ink-light: #ffffff;
    --rule-red: rgba(255, 255, 255, 0.22);
    --rule-blue: rgba(255, 255, 255, 0.55);
    --pool-top: #8a93a8;
    --pool-mid: #6f8fb8;
    --pool-water: #2f7fb4;
    --pool-deep: #3d5f9a;
  }
  * { margin: 0; padding: 0; box-sizing: border-box; }
  html, body { width: 1200px; height: 928px; overflow: hidden; background: var(--paper); }
  body { font-family: "Source Sans 3", "Calibri", sans-serif; color: var(--ink-light); position: relative; }

  .page { position: absolute; top: 22px; width: 560px; height: 884px; overflow: hidden; }
  .page--front { left: 22px; background: var(--crimson); }
  .page--back { left: 618px; }

  .front-base { position: absolute; left: 0; bottom: 0; width: 560px; height: 110px; }

  .title {
    position: absolute; right: 36px; top: 36px;
    font-size: 54px; font-weight: 600; color: var(--crimson-title);
    text-shadow: 1px 1px 0 #c21a1a, -1px -1px 0 #5a0000, 2px 3px 4px rgba(0,0,0,0.35);
    letter-spacing: 0.5px;
  }
  .tagline { position: absolute; right: 38px; top: 142px; font-size: 24px; color: var(--blush); }

  .section { position: absolute; }
  .section h2 { font-size: 34px; font-weight: 400; line-height: 1; margin-bottom: 12px; }
  .items { list-style: none; }
  .items li {
    display: flex; justify-content: space-between; align-items: center;
    height: 29px; padding: 0 8px 0 17px; font-size: 17px;
    border-bottom: 1px solid var(--rule-red);
  }
  .items li:last-child { border-bottom: none; }
  .items .price { font-size: 18px; }

  .page--front .section { left: 57px; width: 468px; }
  .sec-desserts { top: 193px; }
  .sec-pies { top: 366px; }

  .brand-mark {
    position: absolute; left: 0; width: 560px; top: 690px; text-align: center;
    font-size: 34px; font-weight: 600; color: var(--ink-light);
  }

  .pool-scene {
    position: absolute; inset: 0;
    background: linear-gradient(180deg, var(--pool-top) 0%, var(--pool-mid) 40%, var(--pool-water) 58%, var(--pool-deep) 100%);
  }
  .page--back .section { left: 56px; width: 464px; }
  .page--back .items li { border-bottom-color: var(--rule-blue); padding-right: 12px; }
  .sec-salads { top: 100px; }
  .sec-cocktails { top: 275px; }
  .sec-juices { top: 451px; }
  .back-brand {
    position: absolute; right: 38px; top: 56px;
    font-size: 22px; font-weight: 600; color: var(--ink-light);
  }
</style>
</head>
<body>
  <section class="page page--front">
    <h1 class="title">Kelari Vostina</h1>
    <p class="tagline">Chania, Crete in Greece</p>

    <div class="section sec-desserts">
      <h2>Desserts</h2>
      <ul class="items">
        <li><span>Tahitian Vanilla Ice</span><span class="price">$10</span></li>
        <li><span>Cream</span><span class="price">$10</span></li>
        <li><span>Roasted Almonds</span><span class="price">$10</span></li>
        <li><span>Chocolate Sauce</span><span class="price">$10</span></li>
      </ul>
    </div>

    <div class="section sec-pies">
      <h2>Pies</h2>
      <ul class="items">
        <li><span>Tahitian Vanilla Ice</span><span class="price">$10</span></li>
        <li><span>Cream</span><span class="price">$10</span></li>
        <li><span>Roasted Almonds</span><span class="price">$10</span></li>
        <li><span>Chocolate Sauce</span><span class="price">$10</span></li>
      </ul>
    </div>

    <p class="brand-mark">Kelari Vostina</p>

    <svg class="front-base" viewBox="0 0 560 110" aria-hidden="true">
      <ellipse cx="280" cy="48" rx="60" ry="8" fill="rgba(0,0,0,0.35)"/>
      <path d="M0 58 Q280 -12 560 58 L560 110 L0 110 Z" fill="var(--crimson-deep)"/>
    </svg>
  </section>

  <section class="page page--back">
    <div class="pool-scene" role="img" aria-label="Photo of a mojito and a strawberry daiquiri on a poolside table, blurred pool behind"></div>
    <p class="back-brand">Kelari Vostina</p>

    <div class="section sec-salads">
      <h2>Salads</h2>
      <ul class="items">
        <li><span>Tahitian Vanilla Ice</span><span class="price">$10</span></li>
        <li><span>Cream</span><span class="price">$10</span></li>
        <li><span>Roasted Almonds</span><span class="price">$10</span></li>
        <li><span>Chocolate Sauce</span><span class="price">$10</span></li>
      </ul>
    </div>

    <div class="section sec-cocktails">
      <h2>Cocktails</h2>
      <ul class="items">
        <li><span>Tahitian Vanilla Ice</span><span class="price">$10</span></li>
        <li><span>Cream</span><span class="price">$10</span></li>
        <li><span>Roasted Almonds</span><span class="price">$10</span></li>
        <li><span>Chocolate Sauce</span><span class="price">$10</span></li>
      </ul>
    </div>

    <div class="section sec-juices">
      <h2>Fresh juices</h2>
      <ul class="items">
        <li><span>Tahitian Vanilla Ice</span><span class="price">$10</span></li>
        <li><span>Cream</span><span class="price">$10</span></li>
        <li><span>Roasted Almonds</span><span class="price">$10</span></li>
        <li><span>Chocolate Sauce</span><span class="price">$10</span></li>
      </ul>
    </div>
  </section>
</body>
</html>
```